Local Trading Business Needs Stationary Designs

We need designs for a new company based in Uganda called "Amber Crest Trading Limited". We are looking to grow into a multinational company that focuses on distributorship of merchandised products within the East African region. We would like to see stationary designs for a Logo, Letterhead, Envelops, File folder, Business cards, receipt and proforma invoice. The final design should communicate boldness and growth.

Industry/Entity Type

Business

Font styles to use
Other font styles liked:
• Helvetica

```html
<!DOCTYPE html>
<html lang="en">
<head>
<meta charset="utf-8">
<title>Amber Crest Trading Limited — Stationery</title>
<link rel="stylesheet" href="https://fonts.googleapis.com/css2?family=Gelasio:wght@400&family=Open+Sans:wght@400;600&display=swap">
<style>
  :root{
    --navy:#1f2d62;
    --navy-card:#233068;
    --brand:#2b3590;
    --ink:#222;
    --paper:#ffffff;
    --backdrop:#3b3b3b;
  }
  *{margin:0;padding:0;box-sizing:border-box}
  html,body{width:1200px;height:999px;overflow:hidden}
  body{background:var(--backdrop);position:relative;font-family:"Open Sans",Helvetica,Arial,sans-serif;color:var(--ink)}
  .sheet{position:absolute;background:var(--paper)}
  .letterhead{left:62px;top:66px;width:649px;height:916px}
  .card-front{left:585px;top:314px;width:275px;height:157px}
  .card-back{left:903px;top:314px;width:275px;height:157px;background:var(--navy-card)}
  .envelope{left:457px;top:505px;width:707px;height:314px}

  .brand{position:absolute;display:flex;align-items:center;color:var(--brand);font-family:"Gelasio",Georgia,serif;font-weight:400}
  .brand-dot{border-radius:50%;background:var(--brand);flex:none}
  .brand-name{display:flex;flex-direction:column;line-height:1}
  .brand-name .sub{text-transform:uppercase;letter-spacing:.01em}

  .rule{position:absolute;left:0;right:0;background:var(--navy)}
  .small{position:absolute;font-size:9px;line-height:1.35;font-weight:600}
  .contact{position:absolute;display:flex;flex-direction:column}
  .contact-row{display:flex;align-items:center;gap:6px;font-weight:600}
  .contact svg{flex:none;fill:var(--ink)}

  /* letterhead */
  .letterhead .brand{left:18px;top:26px;gap:8px}
  .letterhead .brand-dot{width:48px;height:48px}
  .letterhead .brand-name .main{font-size:31px}
  .letterhead .brand-name .sub{font-size:13px;margin-top:3px}
  .letterhead .address{left:44px;top:858px}
  .letterhead .globe-icon{position:absolute;left:22px;top:862px}
  .letterhead .contact{left:166px;top:857px;gap:3px;font-size:9px}

  /* card front */
  .card-front .brand{left:10px;top:11px;gap:5px}
  .card-front .brand-dot{width:30px;height:30px}
  .card-front .brand-name .main{font-size:19px}
  .card-front .brand-name .sub{font-size:8px;margin-top:2px}
  .card-front .person{position:absolute;left:15px;top:77px}
  .card-front .person .name{font-size:12px}
  .card-front .person .role{font-size:7px;font-weight:600}
  .card-front .address{left:15px;top:116px;font-size:7.5px}
  .card-front .contact{left:173px;top:102px;gap:2px;font-size:7.5px}

  /* card back */
  .card-back .brand{left:48px;top:55px;gap:7px;color:#fff}
  .card-back .brand-dot{width:38px;height:38px;background:#fff}
  .card-back .brand-name{align-items:flex-end}
  .card-back .brand-name .main{font-size:25px}
  .card-back .brand-name .sub{font-size:10.5px;margin-top:3px}

  /* envelope */
  .envelope .brand{left:14px;top:207px;gap:7px}
  .envelope .brand-dot{width:50px;height:50px}
  .envelope .brand-name .main{font-size:30px}
  .envelope .brand-name .sub{font-size:13px;margin-top:3px}
  .envelope .address{left:19px;top:265px;font-size:10px;font-weight:400}
</style>
</head>
<body>

<section class="sheet letterhead">
  <div class="brand">
    <span class="brand-dot"></span>
    <span class="brand-name"><span class="main">Amber Crest</span><span class="sub">Trading Limited</span></span>
  </div>
  <svg class="globe-icon" width="16" height="16" viewBox="0 0 16 16" fill="none" stroke="#222" stroke-width="1.2"><circle cx="8" cy="8" r="7"/><ellipse cx="8" cy="8" rx="3" ry="7"/><path d="M1 8h14M2.5 4.5h11M2.5 11.5h11"/></svg>
  <p class="small address">suit # 00, Lorem ipsum<br>Lorem Lorem ipsum</p>
  <div class="contact">
    <span class="contact-row"><svg width="10" height="10" viewBox="0 0 10 10"><rect width="10" height="10" rx="2"/><path d="M3 2.5c0 2.5 2 4.5 4.5 4.5" stroke="#fff" stroke-width="1.3" fill="none"/></svg>000-000-0000</span>
    <span class="contact-row"><svg width="10" height="10" viewBox="0 0 10 10"><path d="M2 0l6 6H5l2 4-1.5.6-2-4L2 8z"/></svg>www.ambercrest.com</span>
  </div>
  <div class="rule" style="top:890px;height:2px"></div>
  <div class="rule" style="top:894px;height:22px"></div>
</section>

<section class="sheet card-front">
  <div class="brand">
    <span class="brand-dot"></span>
    <span class="brand-name"><span class="main">Amber Crest</span><span class="sub">Trading Limited</span></span>
  </div>
  <div class="person"><p class="name">Title Name</p><p class="role">designation</p></div>
  <p class="small address">suit # 00, Lorem ipsum<br>Lorem Lorem ipsum</p>
  <div class="contact">
    <span class="contact-row"><svg width="8" height="8" viewBox="0 0 10 10"><rect width="10" height="10" rx="2"/><path d="M3 2.5c0 2.5 2 4.5 4.5 4.5" stroke="#fff" stroke-width="1.3" fill="none"/></svg>000-000-0000</span>
    <span class="contact-row"><svg width="8" height="8" viewBox="0 0 10 10"><rect width="10" height="10" rx="2"/><path d="M2 3l3 2.5L8 3" stroke="#fff" stroke-width="1.2" fill="none"/></svg>abcd@ambercrest.com</span>
    <span class="contact-row"><svg width="8" height="8" viewBox="0 0 10 10"><path d="M2 0l6 6H5l2 4-1.5.6-2-4L2 8z"/></svg>www.ambercrest.com</span>
  </div>
  <div class="rule" style="top:142px;height:1px"></div>
  <div class="rule" style="top:145px;height:12px"></div>
</section>

<section class="sheet card-back">
  <div class="brand">
    <span class="brand-dot"></span>
    <span class="brand-name"><span class="main">Amber Crest</span><span class="sub">Trading Limited</span></span>
  </div>
</section>

<section class="sheet envelope">
  <div class="brand">
    <span class="brand-dot"></span>
    <span class="brand-name"><span class="main">Amber Crest</span><span class="sub">Trading Limited</span></span>
  </div>
  <p class="small address">suit # 00, Lorem ipsum Lorem Lorem ipsum</p>
  <div class="rule" style="top:287px;height:3px"></div>
  <div class="rule" style="top:293px;height:21px"></div>
</section>

</body>
</html>
```